Medical business needs responsive Bootstrap theme design

We need a responsive Twitter Bootstrap theme for a hair transplant business in South Korea which looks good from full size desktop screens down to smartphone displays. We would like the site to match in style with our brochure design (see the PDF and Adobe Illustrator files), although it does not need to match exactly. Please feel free to use the design elements and images in the brochure. The general flow of the theme is shown in the wireframe image.
We expect graphic design, images, CSS, and HTML. No PHP/backend/ecommerce integration is expected.
Here are the links to the 3 stock images in the brochure:
http://www.pixelvantry.com/pic.mhtml?id=918270563
http://www.lumoframes.com/photo/hair-transplant-gm730418256-61920475
http://www.lumoframes.com/photo/doctor-inspecting-skin-of-head-gm842067319-57301846
You can use the Bootstrap template here as a starting point: http://kelvarnlayouts.com/template-overviews/agency/
Target Market(s)
Our primary customers will be Westerners aged 28-45
Industry/Entity Type
Plastic Surgery
Coding
Coded - Design and coding required
Number of Pages Required
1 page

```html
<!DOCTYPE html>
<html lang="en">
<head>
<meta charset="utf-8">
<title>Lumora Hair Clinic</title>
<link href="https://fonts.googleapis.com/css2?family=Raleway:wght@300;400;600;700&family=Lato:wght@300;400;700&family=Crimson+Text:ital,wght@1,400;1,600&display=swap" rel="stylesheet">
<style>
:root{
  --accent:#1abc9c;
  --red:#d9534f;
  --ink:#333;
  --text:#555;
  --muted:#888;
  --line:#e5e5e5;
  --band:#f5f5f5;
  --footer:#333;
}
*{box-sizing:border-box;margin:0;padding:0}
html,body{width:1200px;height:3338px;overflow:hidden}
body{position:relative;background:#fff;font-family:'Lato',sans-serif;color:var(--text)}
.abs{position:absolute}
.center{left:0;width:1200px;text-align:center}

/* header */
.site-header{top:0;left:0;width:1200px;height:75px;border-bottom:1px solid #eee;background:#fff}
.brand{position:absolute;left:22px;top:20px;display:flex;align-items:center;gap:10px;font:700 20px 'Raleway',sans-serif;color:#2a7fc0;letter-spacing:1px}
.brand-dot{width:28px;height:28px;border-radius:50%;background:#2a7fc0}
.nav{position:absolute;right:57px;top:31px;display:flex;gap:24px;font:700 10.5px 'Raleway',sans-serif;letter-spacing:1px;color:#444}
.nav .active{color:var(--accent)}

/* hero */
.hero{top:75px;left:0;width:1200px;height:522px;background:linear-gradient(100deg,#8b7a5e 0%,#b99a7a 35%,#c9a68c 55%,#bda98a 80%,#d8cfae 100%)}
.hero-title{top:272px;font:700 46px 'Raleway',sans-serif;color:#fff;letter-spacing:1px}
.hero-sub{top:346px;font:300 18px/28px 'Lato',sans-serif;color:rgba(255,255,255,.9)}
.hero-arrow{top:318px;width:39px;height:39px;background:rgba(0,0,0,.35);display:flex;align-items:center;justify-content:center}
.hero-arrow.prev{left:0}.hero-arrow.next{right:0}
.hero-down{top:566px;left:591px}

/* section headings */
.sec-title{font:700 23px 'Raleway',sans-serif;color:var(--ink);letter-spacing:.5px}
.sec-title .hl{color:var(--accent)}
.sec-sub{font:300 16px 'Lato',sans-serif;color:var(--muted)}
.sec-rule{left:581px;width:39px;border-top:2px solid #444}

/* features */
.feature{width:265px}
.photo{display:block;width:100%}
.feature .photo{height:164px}
.feature h4{margin-top:21px;font:700 12px 'Raleway',sans-serif;letter-spacing:1px;color:var(--ink)}
.feature .lead{margin-top:6px;font:400 13px 'Raleway',sans-serif;color:var(--muted);letter-spacing:.5px}
.feature p{margin-top:15px;font:400 10.5px/19px 'Lato',sans-serif;color:#999}
.star-rule{top:1168px;left:406px;width:388px;height:1px;background:var(--line)}
.star-rule svg{position:absolute;left:186px;top:-7px;background:#fff;padding:0 3px}

/* pricing */
.plan{background:#fff;border:1px solid var(--line);text-align:center}
.plan-head{background:var(--band);border-bottom:1px solid var(--line);height:48px;padding-top:14px;font:700 15px 'Raleway',sans-serif;color:var(--ink);letter-spacing:1px}
.plan-price{font:300 46px 'Lato',sans-serif;color:var(--ink);margin-top:18px}
.plan-price sup{font-size:22px;vertical-align:24px}
.plan-price small{font-size:11px;color:var(--muted);margin-left:2px}
.plan ul{list-style:none;margin-top:16px;font:400 10.5px 'Lato',sans-serif;color:#555}
.plan li{height:25px}
.plan li b{font-weight:700}
.plan-foot{position:absolute;left:0;right:0;bottom:0;border-top:1px solid var(--line);background:var(--band)}
.btn{display:block;color:#fff;font:400 13px 'Lato',sans-serif;text-align:center;border-radius:2px}
.btn-red{background:var(--red)}
.btn-accent{background:var(--accent)}
.plan.featured{box-shadow:0 0 8px rgba(0,0,0,.12);z-index:2}
.plan.featured .plan-head{background:#fff;height:74px;padding-top:18px}
.plan.featured .plan-head span{display:block;margin-top:5px;font:400 9px 'Lato',sans-serif;color:#aaa;letter-spacing:.5px}
.plan.featured .plan-price{color:var(--accent);font-size:58px}
.plan.featured .plan-price sup{font-size:20px;vertical-align:30px}
.plan.featured .plan-foot{background:#fff}

/* testimonials */
.t-title{top:1784px;font:400 19px 'Raleway',sans-serif;color:var(--ink)}
.quote{top:1831px;height:145px;border:1px solid var(--line);padding:18px 16px}
.avatar{position:absolute;left:16px;top:18px;width:47px;height:47px;border-radius:50%;background:linear-gradient(#9b8370,#5b4a40)}
.quote blockquote{margin-left:60px;max-width:172px;font:italic 600 12.5px/19px 'Crimson Text',serif;color:#555}
.quote .who{margin:7px 0 0 60px;font:700 9.5px 'Lato',sans-serif;color:#444;letter-spacing:.3px}
.quote .org{margin-left:78px;font:400 8.5px 'Lato',sans-serif;color:#aaa}
.dots{top:1998px;left:591px;display:flex;gap:6px}
.dots i{width:6px;height:6px;border-radius:50%;background:#a8e3d6}
.dots i.on{background:var(--accent)}

/* blog */
.post{width:273px}
.post .photo{height:153px;position:relative}
.post h4{margin-top:24px;font:700 13.5px/20px 'Raleway',sans-serif;letter-spacing:1px;color:var(--ink)}
.meta{margin-top:7px;font:italic 400 10.5px 'Crimson Text',serif;color:#999;display:flex;gap:6px;align-items:center}
.post p{margin-top:22px;font:400 10.5px/19px 'Lato',sans-serif;color:#666}
.more{display:block;margin-top:20px;font:italic 600 12px 'Crimson Text',serif;color:var(--accent);text-decoration:underline}
.post-rule{top:2592px;height:1px;background:var(--line)}
.pager{top:2632px;height:25px;border:1px solid #d6efe8;border-radius:13px;padding:0 11px;font:400 10.5px/23px 'Lato',sans-serif;color:var(--accent)}
.gallery-dots{position:absolute;right:10px;top:10px;display:flex;gap:4px}
.gallery-dots i{width:6px;height:6px;border-radius:50%;border:1px solid #fff}
.gallery-dots i.on{background:#fff}

/* contact */
.form-title{top:2847px;left:168px;width:414px;display:flex;align-items:center;gap:14px;font:400 19px 'Raleway',sans-serif;color:var(--ink)}
.form-title::after{content:"";flex:1;height:7px;background:#f0f0f0}
.label{font:700 9.5px 'Raleway',sans-serif;letter-spacing:1px;color:#444}
.field{border:2px solid #ddd;background:#fff}
.send{top:3139px;left:168px;width:121px;height:30px;background:var(--accent);color:#fff;font:700 10.5px/30px 'Raleway',sans-serif;letter-spacing:1px;text-align:center}
.map{top:2846px;left:617px;width:416px;height:311px;background:linear-gradient(135deg,#ece7dc,#e2ddd0 50%,#d9e3d1)}

/* footer */
.site-footer{top:3226px;left:0;width:1200px;height:112px;background:var(--footer)}
.copy{position:absolute;left:168px;top:38px;font:400 10px/19px 'Lato',sans-serif;color:#666}
.copy span{border-bottom:1px solid #555}
.socials{position:absolute;right:169px;top:40px;display:flex;gap:18px}
.socials i{width:9px;height:9px;border-radius:50%;background:#666}
.contact-line{position:absolute;right:169px;top:66px;font:400 10px 'Lato',sans-serif;color:#666}
</style>
</head>
<body>

<header class="abs site-header">
  <div class="brand"><span class="brand-dot"></span>LUMORA</div>
  <nav class="nav">
    <span class="active">HOME</span><span>ABOUT US</span><span>PORTFOLIO</span><span>PRICING</span><span>BLOG</span><span>CONTACT US</span>
  </nav>
</header>

<section class="abs hero" role="img" aria-label="Photo of a man's hairline being marked out with a comb before a hair transplant"></section>
<h1 class="abs center hero-title">WELCOME TO LUMORA</h1>
<p class="abs center hero-sub">Create just what you need for your Perfect Website. Choose from a wide range<br>of Elements &amp; simply put them on our Lumora.</p>
<div class="abs hero-arrow prev"><svg width="10" height="14"><path d="M8 1 2 7l6 6" fill="none" stroke="#fff" stroke-width="2"/></svg></div>
<div class="abs hero-arrow next"><svg width="10" height="14"><path d="M2 1l6 6-6 6" fill="none" stroke="#fff" stroke-width="2"/></svg></div>
<svg class="abs hero-down" width="18" height="12"><path d="M2 2l7 7 7-7" fill="none" stroke="#fff" stroke-width="2.5"/></svg>

<h2 class="abs center sec-title" style="top:662px">WHY <span class="hl">SOUT KOREA</span></h2>
<p class="abs center sec-sub" style="top:703px">Proin id arcu ac augue fringilla imperdiet at eget nunc</p>
<div class="abs sec-rule" style="top:747px"></div>

<article class="abs feature" style="left:168px;top:788px">
  <div class="photo" role="img" aria-label="Close-up of a comb at a dark hairline marked for transplant" style="background:linear-gradient(180deg,#f4f4f4 0%,#9a8f86 45%,#3a2f2a 75%,#c9a996 100%)"></div>
  <h4>QUALITY OF CARE</h4>
  <div class="lead">Because we are Reliable.</div>
  <p>Lorem ipsum dolor sit amet, consectetur adipisicing elit. Eligendi rem, facilis nobis voluptatum est voluptatem accusamus molestiae eaque perspiciatis mollitia.</p>
</article>
<article class="abs feature" style="left:467px;top:788px">
  <div class="photo" role="img" aria-label="Scalp of a patient shortly after hair transplant surgery" style="background:radial-gradient(ellipse at 50% 55%,#a8705f 0%,#b98a74 35%,#3d3431 65%,#5b7fb5 100%)"></div>
  <h4>CONVENIENCE</h4>
  <div class="lead">To Redefine your Brand.</div>
  <p>Quos, non, esse eligendi ab accusantium voluptatem. Maxime eligendi beatae, atque tempora ullam. Vitae delectus quia, consequuntur rerum molestias quo.</p>
</article>
<article class="abs feature" style="left:766px;top:788px">
  <div class="photo" role="img" aria-label="Doctor's hand pointing at a patient's treated scalp" style="background:radial-gradient(ellipse at 40% 60%,#c97a63 0%,#d99a83 40%,#e8e3e0 75%,#f2f2f2 100%)"></div>
  <h4>COST SAVINGS</h4>
  <div class="lead">Make our Customers Happy.</div>
  <p>Porro repellat vero sapiente amet vitae quibusdam necessitatibus consectetur, labore totam. Accusamus perspiciatis asperiores labore esse ab accusantium ea modi ut.</p>
</article>

<div class="abs star-rule"><svg width="16" height="14" viewBox="0 0 24 24"><path d="M12 2l3 7h7l-5.5 4.5 2 7.5L12 16.5 5.5 21l2-7.5L2 9h7z" fill="#ddd"/></svg></div>

<h2 class="abs center sec-title" style="top:1243px">PRICING</h2>
<p class="abs center sec-sub" style="top:1283px">We offer Flexible Pricing Options.</p>
<div class="abs sec-rule" style="top:1327px"></div>

<div class="abs plan" style="left:168px;top:1383px;width:288px;height:342px">
  <div class="plan-head">STARTER</div>
  <div class="plan-price"><sup>€</sup>7<small>/mo</small></div>
  <ul><li><b>Full</b> Access</li><li>&lt;/&gt; Source Files</li><li><b>100</b> User Accounts</li><li><b>1 Year</b> License</li><li>Phone &amp; Email Support</li></ul>
  <div class="plan-foot" style="height:60px"><a class="btn btn-red" style="margin:12px 23px 0;height:35px;line-height:35px">Sign Up</a></div>
</div>
<div class="abs plan featured" style="left:455px;top:1367px;width:290px;height:379px">
  <div class="plan-head">PROFESSIONAL<span>MOST POPULAR</span></div>
  <div class="plan-price"><sup>€</sup>12<small>/mo</small></div>
  <ul style="margin-top:18px"><li><b>Full</b> Access</li><li>&lt;/&gt; Source Files</li><li><b>1000</b> User Accounts</li><li><b>2 Years</b> License</li>
    <li><svg width="60" height="11" viewBox="0 0 60 11" fill="#555"><g id="s"><path d="M5.5 0l1.6 3.6 3.9.3-3 2.6.9 3.9-3.4-2.1-3.4 2.1.9-3.9-3-2.6 3.9-.3z"/></g><use href="#s" x="12"/><use href="#s" x="24"/><use href="#s" x="36"/><use href="#s" x="48"/></svg></li></ul>
  <div class="plan-foot" style="height:60px"><a class="btn btn-accent" style="margin:12px 24px 0;height:35px;line-height:35px">Sign Up</a></div>
</div>
<div class="abs plan" style="left:745px;top:1383px;width:288px;height:342px">
  <div class="plan-head">BUSINESS</div>
  <div class="plan-price"><sup>€</sup>19<small>/mo</small></div>
  <ul><li><b>Full</b> Access</li><li>&lt;/&gt; Source Files</li><li><b>500</b> User Accounts</li><li><b>3 Years</b> License</li><li>Phone &amp; Email Support</li></ul>
  <div class="plan-foot" style="height:60px"><a class="btn btn-red" style="margin:12px 23px 0;height:35px;line-height:35px">Sign Up</a></div>
</div>

<h3 class="abs center t-title">Testimonials</h3>
<div class="abs quote" style="left:168px;width:279px">
  <div class="avatar" role="img" aria-label="Customer portrait"></div>
  <blockquote>"Incidunt deleniti blanditiis quas aperiam recusandae consequatur ullam quibusdam cum libero illo rerum repellendus!"</blockquote>
  <div class="who">– DARA WHITCOMBE</div><div class="org">Brastow Inc.</div>
</div>
<div class="abs quote" style="left:461px;width:278px">
  <div class="avatar" role="img" aria-label="Customer portrait"></div>
  <blockquote>"Natus voluptatum enim quod necessitatibus quis expedita harum provident eos obcaecati id culpa corporis molestias."</blockquote>
  <div class="who">– MAREK OLSVIK</div><div class="org">Quillmere Inc.</div>
</div>
<div class="abs quote" style="left:754px;width:279px">
  <div class="avatar" role="img" aria-label="Customer portrait"></div>
  <blockquote>"Fugit officia dolor sed harum excepturi ex iusto magnam asperiores molestiae qui natus obcaecati facere sint amet."</blockquote>
  <div class="who">– LENA BROOKFIELD</div><div class="org">Orvalen Inc.</div>
</div>
<div class="abs dots"><i class="on"></i><i></i></div>

<h2 class="abs center sec-title" style="top:2074px">BLOG</h2>
<p class="abs center sec-sub" style="top:2114px">Our Latest News</p>
<div class="abs sec-rule" style="top:2158px"></div>

<article class="abs post" style="left:168px;top:2198px">
  <div class="photo" role="img" aria-label="Comb at a hairline marked for transplant" style="background:linear-gradient(180deg,#f4f4f4 0%,#9a8f86 45%,#3a2f2a 75%,#c9a996 100%)"></div>
  <h4>THIS IS A STANDARD POST WITH A PREVIEW IMAGE</h4>
  <div class="meta">10th Feb 2014 <span>/</span> 13 <span>/</span></div>
  <p>Lorem ipsum dolor sit amet, consectetur adipisicing elit. Ratione, voluptatem, dolorem animi nisi autem blanditiis enim culpa reiciendis et explicabo tenetur!</p>
  <a class="more">Read More</a>
</article>
<article class="abs post" style="left:464px;top:2198px">
  <div class="photo" role="img" aria-label="Embedded video of a night sky over mountains" style="background:linear-gradient(180deg,#1d2233 0%,#33405a 55%,#3a3530 80%,#1a1a1a 100%)"></div>
  <h4>THIS IS A STANDARD POST WITH A STREAMLY VIDEO</h4>
  <div class="meta">16th Feb 2014 <span>/</span> 19 <span>/</span></div>
  <p>Lorem ipsum dolor sit amet, consectetur adipisicing elit. Ratione, voluptatem, dolorem animi nisi autem blanditiis enim culpa reiciendis et explicabo tenetur!</p>
  <a class="more">Read More</a>
</article>
<article class="abs post" style="left:759px;top:2198px">
  <div class="photo" role="img" aria-label="Gallery of post-surgery scalp photos" style="background:radial-gradient(ellipse at 50% 55%,#a8705f 0%,#b98a74 35%,#3d3431 65%,#5b7fb5 100%)"><div class="gallery-dots"><i></i><i></i><i class="on"></i></div></div>
  <h4>THIS IS A STANDARD POST WITH A SLIDER GALLERY</h4>
  <div class="meta">24th Feb 2014 <span>/</span> 21 <span>/</span></div>
  <p>Lorem ipsum dolor sit amet, consectetur adipisicing elit. Ratione, voluptatem, dolorem animi nisi autem blanditiis enim culpa reiciendis et explicabo tenetur!</p>
  <a class="more">Read More</a>
</article>
<div class="abs post-rule" style="left:168px;width:273px"></div>
<div class="abs post-rule" style="left:464px;width:273px"></div>
<div class="abs post-rule" style="left:759px;width:274px"></div>
<div class="abs pager" style="left:168px">← Older</div>
<div class="abs pager" style="right:167px">Newer →</div>

<h2 class="abs center sec-title" style="top:2722px">GET IN TOUCH WITH US</h2>
<p class="abs center sec-sub" style="top:2762px">Still have Questions? Contact Us using the Form below.</p>
<div class="abs sec-rule" style="top:2806px"></div>

<h3 class="abs form-title">Send us an Email</h3>
<div class="abs label" style="left:168px;top:2899px">NAME *</div>
<div class="abs label" style="left:311px;top:2899px">EMAIL *</div>
<div class="abs label" style="left:455px;top:2899px">PHONE</div>
<div class="abs field" style="left:168px;top:2920px;width:127px;height:31px"></div>
<div class="abs field" style="left:311px;top:2920px;width:127px;height:31px"></div>
<div class="abs field" style="left:455px;top:2920px;width:127px;height:31px"></div>
<div class="abs label" style="left:168px;top:2974px">MESSAGE *</div>
<div class="abs field" style="left:168px;top:2994px;width:414px;height:125px"></div>
<div class="abs send">SEND MESSAGE</div>
<div class="abs map" role="img" aria-label="Street map showing the clinic location"></div>

<footer class="abs site-footer">
  <div class="copy">Copyrights © 2016 All Rights Reserved by Lumora Studio.<br><span>Terms of Use</span> / <span>Privacy Policy</span></div>
  <div class="socials"><i></i><i></i><i></i><i></i><i></i><i></i><i></i><i></i></div>
  <div class="contact-line">✉ hello@lumorahair.com · ☎ +82-2-555-0147 · Callpoint</div>
</footer>

</body>
</html>
```